Stridewell Specialists Stationary

At Stridewell Specs, we know that rehab technology is much more than a tool or machine. It’s mobility for your body and productivity and freedom for your lifestyle to reclaim your life. That’s why we specialize in custom power and manual wheelchairs, scooters, complex seating and positioning, standers, and bathroom equipment that all help you reclaim your life.

Our rehab equipment includes custom power wheelchairs offering complex, customized seating and positioning systems with an array of specialized electronic control features. With a certified staff of Assistive Technology Professionals (ATPs) and technical repair department, we provide knowledgeable assistance to make sure you get the right products needed to reclaim your life – delivered on time, right to your door.

```html
<!DOCTYPE html>
<html lang="en">
<head>
<meta charset="utf-8">
<title>Stridewell Specialists Stationery</title>
<link href="https://fonts.googleapis.com/css2?family=Montserrat:wght@400;500;600&family=Great+Vibes&display=swap" rel="stylesheet">
<style>
  :root {
    --navy: #1c2b55;
    --green: #8dc63f;
    --paper: #f4f4f3;
    --backdrop: #cdcdcf;
    --ink: #4a4a4a;
  }
  * { margin: 0; padding: 0; box-sizing: border-box; }
  html, body { width: 1200px; height: 1000px; overflow: hidden; }
  body {
    background: var(--backdrop);
    font-family: "Montserrat", Arial, sans-serif;
    color: var(--ink);
    position: relative;
  }
  .sheet { position: absolute; background: var(--paper); overflow: hidden; }
  .stripe { position: absolute; left: 0; width: 100%; display: block; }

  .brand { position: absolute; display: flex; align-items: center; gap: 4px; color: var(--navy); font-weight: 600; }
  .brand-dot { border-radius: 50%; background: var(--green); flex: none; }
  .brand-name { line-height: 1; }
  .brand-name span { display: block; }
  .brand-sub { letter-spacing: 0.18em; margin-top: 2px; }

  .contact { position: absolute; font-size: 5px; line-height: 7px; color: #333; white-space: nowrap; }
  .contact li { list-style: none; display: flex; align-items: center; gap: 3px; }
  .icon { width: 5px; height: 5px; background: var(--green); display: inline-block; border-radius: 1px; flex: none; }
  .address { position: absolute; font-size: 5px; line-height: 6.5px; color: #333; white-space: nowrap; }

  /* letterhead */
  .letterhead { left: 232px; top: 55px; width: 340px; height: 483px; }
  .letter-body { position: absolute; left: 31px; top: 160px; width: 278px; font-size: 5.1px; line-height: 6.6px; color: #555; text-align: justify; }
  .letter-body p { margin-bottom: 6px; }
  .letter-sign { position: absolute; left: 31px; top: 310px; font-size: 5.1px; line-height: 6.4px; color: #555; }
  .letter-sign strong { color: #222; font-weight: 600; }
  .signature-area { position: absolute; left: 76px; top: 303px; width: 66px; height: 30px; background: linear-gradient(90deg, rgba(80,100,200,0.10), rgba(80,100,200,0.04)); }

  /* folder */
  .folder { left: 614px; top: 42px; width: 372px; height: 494px; }
  .folder-spine { position: absolute; left: 26px; top: 0; width: 1px; height: 196px; background: #dcdcdc; }
  .folder-base { position: absolute; left: 0; top: 201px; width: 100%; height: 293px; background: var(--navy); }

  /* envelopes */
  .envelope-front { left: 215px; top: 580px; width: 357px; height: 178px; }
  .envelope-back { left: 614px; top: 580px; width: 358px; height: 178px; }
  .flap { position: absolute; left: 0; top: 0; width: 100%; height: 70px; }
  .flap-dot { position: absolute; left: 172px; top: 18px; width: 12px; height: 12px; border-radius: 50%; background: var(--green); }

  /* business cards */
  .card-front { left: 238px; top: 800px; width: 147px; height: 80px; }
  .card-back { left: 426px; top: 800px; width: 147px; height: 80px; background: var(--navy); }
  .card-person { position: absolute; left: 90px; top: 22px; font-size: 4.6px; line-height: 5.6px; color: #555; white-space: nowrap; }
  .card-person strong { color: var(--green); font-weight: 600; display: block; font-size: 5px; }
  .card-address { position: absolute; left: 8px; top: 44px; width: 70px; text-align: right; font-size: 3.6px; line-height: 5px; color: #444; white-space: nowrap; }
  .card-contact { position: absolute; left: 90px; top: 42px; font-size: 3.6px; line-height: 5.2px; color: #444; white-space: nowrap; }
  .card-contact li { list-style: none; display: flex; gap: 2px; align-items: center; }
  .card-contact .icon { width: 3.5px; height: 3.5px; }

  /* pencil */
  .pencil { position: absolute; left: 258px; top: 924px; width: 296px; height: 10px; }

  /* compliments slip */
  .comp-slip { left: 614px; top: 800px; width: 342px; height: 160px; }
  .compliments { position: absolute; left: 20px; top: 125px; font-family: "Great Vibes", cursive; font-size: 19px; color: var(--navy); }
  .compliments em { font-style: normal; color: var(--green); }
</style>
</head>
<body>

  <!-- Letterhead -->
  <section class="sheet letterhead">
    <div class="brand" style="left:31px; top:28px;">
      <span class="brand-dot" style="width:8px;height:8px;"></span>
      <span class="brand-name" style="font-size:17px;"><span>Stridewell</span><span class="brand-sub" style="font-size:6px;">SPECIALISTS</span></span>
    </div>
    <ul class="contact" style="left:248px; top:35px;">
      <li><i class="icon"></i>+61 812-555-0190</li>
      <li><i class="icon"></i>info@stridewell.com</li>
      <li><i class="icon"></i>www.stridewell.com</li>
    </ul>
    <p class="address" style="left:248px; top:58px;">48 Harbor Point Drive #210<br>Glenfield IL 60112</p>

    <div class="letter-body">
      <p style="color:#222;">Dear sir,</p>
      <p>Thank you for choosing Stridewell Specs for your mobility needs. Our team has reviewed the seating assessment from your recent visit and prepared a set of options for a custom power wheelchair that suits your daily routine, your home and the places you travel most often.</p>
      <p>Each option includes complex seating and positioning, specialized electronic controls and a service plan from our technical repair department. A certified Assistive Technology Professional will walk you through every feature, answer your questions and arrange a trial so you can feel the difference before any decision is made.</p>
      <p>Once you approve a model, we handle the paperwork with your provider and schedule delivery right to your door. Our staff will fit the chair, adjust the seating and make sure you are comfortable and confident on the first day.</p>
      <p>Please call us or reply by email to book your trial. We look forward to helping you reclaim your life.</p>
    </div>
    <p class="letter-sign">Yours Sincerely,<br><strong>Nora Bellamy</strong></p>
    <div class="signature-area" role="img" aria-label="Handwritten signature"></div>

    <svg class="stripe" style="bottom:0; height:7px;" viewBox="0 0 100 6" preserveAspectRatio="none">
      <polygon points="0,3 68,3 66,6 0,6" fill="var(--navy)"/>
      <polygon points="67.5,0 100,0 100,6 65.5,6" fill="var(--green)"/>
    </svg>
  </section>

  <!-- Presentation folder -->
  <section class="sheet folder">
    <div class="folder-spine"></div>
    <div class="brand" style="left:176px; top:56px;">
      <span class="brand-dot" style="width:12px;height:12px;"></span>
      <span class="brand-name" style="font-size:28px;"><span>Stridewell</span><span class="brand-sub" style="font-size:9px;">SPECIALISTS</span></span>
    </div>
    <svg class="stripe" style="top:194px; height:8px;" viewBox="0 0 100 6" preserveAspectRatio="none">
      <polygon points="0,3 41,3 39,6 0,6" fill="var(--navy)"/>
      <polygon points="40.5,0 100,0 100,6 38.5,6" fill="var(--green)"/>
    </svg>
    <div class="folder-base"></div>
  </section>

  <!-- Envelope front -->
  <section class="sheet envelope-front">
    <div class="brand" style="left:17px; top:20px;">
      <span class="brand-dot" style="width:7px;height:7px;"></span>
      <span class="brand-name" style="font-size:15px;"><span>Stridewell</span><span class="brand-sub" style="font-size:5.5px;">SPECIALISTS</span></span>
    </div>
    <p class="address" style="left:17px; top:154px;">48 Harbor Point Drive #210<br>Glenfield IL 60112</p>
    <svg class="stripe" style="bottom:0; height:6px;" viewBox="0 0 100 6" preserveAspectRatio="none">
      <polygon points="0,3 70,3 68,6 0,6" fill="var(--navy)"/>
      <polygon points="69.5,0 100,0 100,6 67.5,6" fill="var(--green)"/>
    </svg>
  </section>

  <!-- Envelope back -->
  <section class="sheet envelope-back">
    <svg class="flap" viewBox="0 0 358 70" preserveAspectRatio="none">
      <polygon points="0,0 358,0 344,62 336,68 22,68 14,62" fill="var(--navy)"/>
    </svg>
    <span class="flap-dot"></span>
  </section>

  <!-- Business card front -->
  <section class="sheet card-front">
    <div class="brand" style="left:14px; top:20px;">
      <span class="brand-dot" style="width:5px;height:5px;"></span>
      <span class="brand-name" style="font-size:10px;"><span>Stridewell</span><span class="brand-sub" style="font-size:3.8px;">SPECIALISTS</span></span>
    </div>
    <p class="card-person"><strong>OWEN RIDLEY</strong>Managing Director</p>
    <p class="card-address">48 Harbor Point Drive #210<br>Glenfield IL 60112</p>
    <ul class="card-contact">
      <li><i class="icon"></i>+61 812-555-0190</li>
      <li><i class="icon"></i>info@stridewell.com</li>
      <li><i class="icon"></i>www.stridewell.com</li>
    </ul>
    <svg class="stripe" style="bottom:0; height:4px;" viewBox="0 0 100 6" preserveAspectRatio="none">
      <polygon points="0,3 56,3 53,6 0,6" fill="var(--navy)"/>
      <polygon points="55,0 100,0 100,6 52,6" fill="var(--green)"/>
    </svg>
  </section>

  <!-- Business card back -->
  <section class="sheet card-back">
    <div class="brand" style="left:38px; top:28px; color:#fff;">
      <span class="brand-dot" style="width:6px;height:6px;"></span>
      <span class="brand-name" style="font-size:12px;"><span>Stridewell</span><span class="brand-sub" style="font-size:4.4px;">SPECIALISTS</span></span>
    </div>
  </section>

  <!-- Pencil -->
  <svg class="pencil" viewBox="0 0 296 10">
    <rect x="0" y="1" width="272" height="8" rx="1.5" fill="var(--navy)"/>
    <polygon points="272,1 292,5 272,9" fill="#e3c9a3"/>
    <polygon points="286,3.8 296,5 286,6.2" fill="#333"/>
  </svg>

  <!-- Compliments slip -->
  <section class="sheet comp-slip">
    <ul class="contact" style="left:20px; top:26px;">
      <li><i class="icon"></i>+61 812-555-0190</li>
      <li><i class="icon"></i>info@stridewell.com</li>
      <li><i class="icon"></i>www.stridewell.com</li>
    </ul>
    <p class="address" style="left:92px; top:26px;">48 Harbor Point Drive #210<br>Glenfield IL 60112</p>
    <div class="brand" style="left:226px; top:20px;">
      <span class="brand-dot" style="width:7px;height:7px;"></span>
      <span class="brand-name" style="font-size:15px;"><span>Stridewell</span><span class="brand-sub" style="font-size:5.5px;">SPECIALISTS</span></span>
    </div>
    <p class="compliments"><em>With</em> Compliments</p>
    <svg class="stripe" style="bottom:0; height:7px;" viewBox="0 0 100 6" preserveAspectRatio="none">
      <polygon points="0,3 53,3 51,6 0,6" fill="var(--navy)"/>
      <polygon points="52.5,0 100,0 100,6 50.5,6" fill="var(--green)"/>
    </svg>
  </section>

</body>
</html>
```